Two Day Training Event includes a Dinner/Bowling Party at Pinhollow in Troy, MI

I would like a postcard to attract Insurance Agents to an KRV meeting calling it a summit or something like that. Just something to mail to insurance agents telling them about our upcoming event with over 20 carriers. An opportunity to certify face to face with MAPD carriers and see what 2020 has to offer. Prior to OEP OPen Enrollment and AEP Annual Election period we have a number of meetings. Carriers want to come especially if we can get a number of agents. We are going to go to Pinhollow a fun bowling alley for dinner, drinks and bowling to network and talk about the upcoming year.

Target Market(s)

Existing and new insurance agents

Industry/Entity Type

Insurance Broker

Contact Information for Business Card

Looking for a new card design I sent my LOGO and can upload my existing card.

Font styles to use
Serif

Colors

Designer to choose colors to be used in the design.

Requirements
Must have
• Dates Sept 16 and 17th
• location Larkfield Conference Hall in Troy MI
• times
Nice to have
• It would be nice to see a fun design.

```html
<!DOCTYPE html>
<html lang="en">
<head>
<meta charset="utf-8">
<title>KRV Agent Summit – Postcard and Business Card</title>
<link rel="stylesheet" href="https://fonts.googleapis.com/css2?family=Open+Sans:wght@400&family=Playfair+Display:wght@400;700&family=Noto+Sans:wght@700&display=swap">
<style>
  :root{
    --board:#808185;
    --paper:#ffffff;
    --sun:#fddd1a;
    --iris:#6666ff;
    --band:#5d5de6;
    --brand:#2b2bd0;
    --ink:#111111;
    --gold:#f7d117;
    --photo-dark:#3a3d44;
    --photo-mid:#8a8078;
    --photo-pale:#e9e9ee;
    --photo-paler:#f4f4f7;
  }
  *{margin:0;padding:0;box-sizing:border-box}
  html,body{width:1200px;height:1200px;overflow:hidden;background:var(--board)}
  .board{position:relative;width:1200px;height:1200px;background:var(--board)}
  .section-title{
    position:absolute;transform:translateX(-50%);
    font-family:"Open Sans",sans-serif;font-weight:400;font-size:29px;
    color:#fff;white-space:nowrap;letter-spacing:-0.3px;
  }
  .card{position:absolute;background:var(--paper);box-shadow:-7px 7px 7px rgba(0,0,0,.55);overflow:hidden}
  .card svg{display:block;width:100%;height:100%}
  .postcard-front{left:62px;top:151px;width:510px;height:362px}
  .postcard-back{left:628px;top:151px;width:510px;height:362px}
  .business-card{left:338px;top:736px;width:521px;height:312px}
  .serif{font-family:"Playfair Display",serif}
  .sans{font-family:"Noto Sans",sans-serif;font-weight:700}
</style>
</head>
<body>
<main class="board">

  <h2 class="section-title" style="left:304px;top:90px">POST-CARD FRONT</h2>
  <h2 class="section-title" style="left:869px;top:90px">POST-CARD BACK</h2>
  <h2 class="section-title" style="left:593px;top:677px">BUSINESS CARD</h2>

  <!-- Postcard front -->
  <section class="card postcard-front">
    <svg viewBox="0 0 821 583" xmlns="http://www.w3.org/2000/svg">
      <defs>
        <linearGradient id="frontPhotoTone" x1="0" y1="0" x2="1" y2="1">
          <stop offset="0" stop-color="var(--photo-dark)"/>
          <stop offset="0.55" stop-color="var(--photo-mid)"/>
          <stop offset="1" stop-color="var(--photo-dark)"/>
        </linearGradient>
      </defs>
      <rect width="821" height="583" fill="var(--paper)"/>
      <polygon role="img" aria-label="Photo of smiling agents networking at an event"
               points="0,0 440,0 153,228 153,350 0,457" fill="url(#frontPhotoTone)"/>
      <polygon class="stripe-yellow" points="440,0 653,0 208,350 153,350 153,228" fill="var(--sun)"/>
      <polygon class="stripe-blue" points="653,0 770,0 56,583 0,583 0,457 153,350 208,350" fill="var(--iris)"/>
      <polygon class="corner-yellow" points="273,407 498,583 56,583" fill="var(--sun)"/>

      <g class="brand-name" fill="var(--brand)" font-family="Playfair Display, serif" font-weight="400">
        <text x="620" y="155" font-size="44">KRV</text>
        <text x="727" y="141" font-size="11">Keystone Ridge</text>
        <text x="727" y="154" font-size="11">Ventures</text>
      </g>

      <g class="agent-details serif" fill="var(--ink)" font-size="14" text-anchor="end" letter-spacing="2.4">
        <text x="796" y="247">DALE WHITCOMBE</text>
        <text x="796" y="274">LICENSED HEALTH AND LIFE AGENT</text>
        <text x="796" y="302">HEALTH AND MEDICARE SPECIALIST</text>
      </g>

      <g class="event-details serif" fill="var(--ink)" font-size="15" text-anchor="end">
        <text x="793" y="433">DATE - SEPT 16 AND 17TH</text>
        <text x="793" y="478">LOCATION - LARKFIELD CONFERENCE</text>
        <text x="793" y="500">HALL IN TROY MI</text>
        <text x="793" y="545">TIME - 3:00 PM</text>
      </g>
    </svg>
  </section>

  <!-- Postcard back -->
  <section class="card postcard-back">
    <svg viewBox="0 0 821 583" xmlns="http://www.w3.org/2000/svg">
      <defs>
        <linearGradient id="backPhotoTone" x1="0" y1="0" x2="1" y2="1">
          <stop offset="0" stop-color="var(--photo-pale)"/>
          <stop offset="0.5" stop-color="var(--photo-paler)"/>
          <stop offset="1" stop-color="var(--photo-pale)"/>
        </linearGradient>
      </defs>
      <rect role="img" aria-label="Faded photo of agents greeting each other" width="821" height="583" fill="url(#backPhotoTone)"/>

      <rect class="stamp-box" x="595" y="33" width="181" height="181" fill="none" stroke="var(--ink)" stroke-width="2"/>

      <g class="brand-name" fill="var(--brand)" font-family="Playfair Display, serif" font-weight="400">
        <text x="59" y="318" font-size="76">KRV</text>
        <text x="258" y="297" font-size="18">Keystone Ridge</text>
        <text x="258" y="318" font-size="18">Ventures</text>
      </g>

      <g class="letter serif" fill="var(--ink)" font-size="12.5">
        <text x="447" y="269">DEAR VALUED CLIENT:</text>
        <text x="447" y="307">I HOPE ALL IS WELL WITH YOU.</text>
        <text x="447" y="345">I AM PROUD TO ANNOUNCE THAT I HAVE JOINED</text>
        <text x="447" y="383">KEYSTONE RIDGE VENTURES, INC. AND I WILL BE</text>
        <text x="447" y="420">ABLE TO EXPAND MY BUSINESS AND OFFER NEW</text>
        <text x="447" y="458">PRODUCTS AND CARRIERS.</text>
      </g>
      <g class="letter-rules" stroke="var(--ink)" stroke-width="1.3">
        <line x1="437" y1="278" x2="778" y2="278"/>
        <line x1="437" y1="316" x2="778" y2="316"/>
        <line x1="437" y1="355" x2="778" y2="355"/>
        <line x1="437" y1="393" x2="778" y2="393"/>
        <line x1="437" y1="434" x2="778" y2="434"/>
        <line x1="437" y1="474" x2="778" y2="474"/>
      </g>

      <rect class="contact-band" x="0" y="507" width="821" height="50" fill="var(--band)"/>
      <g class="contact-band-text" fill="var(--gold)" font-family="Playfair Display, serif" font-weight="700" font-size="13" text-anchor="middle" letter-spacing="4">
        <text x="412" y="525">FAX: (248) 555-0142</text>
        <text x="412" y="551">PHONE: (248) 555-0187 / (800) 555-0163</text>
      </g>
    </svg>
  </section>

  <!-- Business card -->
  <section class="card business-card">
    <svg viewBox="0 0 839 503" xmlns="http://www.w3.org/2000/svg">
      <rect width="839" height="503" fill="var(--paper)"/>
      <polygon class="stripe-yellow" points="419,0 576,0 153,330 112,330 112,237" fill="var(--sun)"/>
      <polygon class="stripe-blue" points="551,22 583,62 40,503 0,503 0,420 153,330" fill="var(--iris)"/>
      <polygon class="corner-yellow" points="198,375 366,503 40,503" fill="var(--sun)"/>

      <g class="brand-name" fill="var(--brand)" font-family="Playfair Display, serif" font-weight="400">
        <text x="36" y="88" font-size="66">KRV</text>
        <text x="205" y="67" font-size="16">Keystone Ridge</text>
        <text x="205" y="86" font-size="16">Ventures</text>
      </g>

      <text class="person-name serif" x="781" y="134" font-size="27" text-anchor="end" letter-spacing="5" fill="var(--ink)">MILES PORTER</text>
      <text class="person-title sans" x="781" y="163" font-size="19" text-anchor="end" letter-spacing="3" fill="var(--ink)">Area manager</text>

      <g class="office-address sans" fill="var(--ink)" font-size="19.5" letter-spacing="1.2">
        <text x="309" y="302">Corporate office</text>
        <text x="309" y="333">1450 Maple Crest Dr.</text>
        <text x="309" y="364">Suite 310</text>
        <text x="309" y="395">Troy,MI 48083</text>
      </g>

      <line class="divider" x1="575" y1="232" x2="575" y2="437" stroke="#999" stroke-width="1.5"/>

      <g class="icons" fill="var(--ink)">
        <!-- office -->
        <g transform="translate(603,314)">
          <rect x="0" y="4" width="7" height="14" fill="none" stroke="var(--ink)" stroke-width="1.4"/>
          <rect x="7" y="0" width="10" height="18" fill="none" stroke="var(--ink)" stroke-width="1.4"/>
          <rect x="10" y="4" width="2" height="2"/><rect x="13" y="4" width="2" height="2"/>
          <rect x="10" y="8" width="2" height="2"/><rect x="13" y="8" width="2" height="2"/>
          <rect x="10" y="12" width="2" height="2"/><rect x="13" y="12" width="2" height="2"/>
        </g>
        <!-- fax -->
        <g transform="translate(603,346)">
          <rect x="4" y="0" width="10" height="6" fill="none" stroke="var(--ink)" stroke-width="1.4"/>
          <rect x="0" y="6" width="18" height="8" rx="1.5" fill="none" stroke="var(--ink)" stroke-width="1.4"/>
          <rect x="4" y="12" width="10" height="5" fill="#fff" stroke="var(--ink)" stroke-width="1.4"/>
        </g>
        <!-- phone -->
        <path transform="translate(603,377)" d="M3 0 L7 0 L8.5 5 L6 7 C7.5 10 9 11.5 12 13 L14 10.5 L19 12 L19 16 C19 17 18 18 17 18 C8 17 1 10 0 2 C0 1 1 0 3 0 Z"/>
        <!-- mail -->
        <g transform="translate(561,461)">
          <rect x="0" y="0" width="18" height="13" fill="var(--ink)"/>
          <polyline points="0.5,0.5 9,7 17.5,0.5" fill="none" stroke="#fff" stroke-width="1.3"/>
        </g>
      </g>

      <g class="phone-numbers sans" fill="var(--ink)" font-size="19.5">
        <text x="634" y="331">(800)555-0163</text>
        <text x="634" y="362">(231)555-0119</text>
        <text x="634" y="393">(248)555-0140</text>
      </g>

      <text class="email sans" x="781" y="475" font-size="17" text-anchor="end" letter-spacing="8.4" fill="var(--ink)">mporter@krvmail.com</text>
    </svg>
  </section>

</main>
</body>
</html>
```